Pebble Reach ~ Business Card Design Project

Pebble Reach is a digital marketing agency which creates and maintains online social presence for brands and businesses. Services include monthly stream management, social media advertising campaigns, online press release distribution, search engine optimization, copywriting, digital strategy consultation, video marketing campaigns, fan acquisition, and Wordpress website development.
The company is currently rebranding to a full service agency from just a social media firm, with a new website launching soon. I'm looking for an extremely creative and modern business card design that pops out from the rest and fits with our company's sector/services.
It will need to be 1039 x 697 pixels, and rectangular (not rounded edges or corners). Utilize our company logo (file is attached), and include the following information in any design or layout:
Mark Telford
CEO/Creative Director
Pebble Reach
Facebook: facebook.com/pebblereach
Twitter: @PebbleReach
Phone: +1 555 014 8832
Cell: +1 555 016 4907
Email: mark@pebblereach.example
Website: www.pebblereach.example
318 Birchmore Avenue, Suite 207
Alderwick, LK
K7Z 4X8

```html
<!DOCTYPE html>
<html lang="en">
<head>
<meta charset="utf-8">
<title>Pebble Reach — Business Card</title>
<link rel="stylesheet" href="https://fonts.googleapis.com/css2?family=Ubuntu:wght@400;500;700&display=swap">
<style>
  :root {
    --bg: #ececec;
    --label: #a9a9a9;
    --white: #ffffff;
    --navy: #25206a;
    --navy-mid: #283a86;
    --blue: #1976bf;
    --blue-light: #1e86cc;
    --ink-name: #2a3a9a;
    --ink-role: #1a7fc7;
    --brand: #2f3f9e;
    --icon: #3f7fc0;
  }
  * { box-sizing: border-box; margin: 0; padding: 0; }
  html, body { width: 1200px; height: 900px; overflow: hidden; }
  body {
    background: var(--bg);
    font-family: "Ubuntu", sans-serif;
    position: relative;
  }
  .side-label {
    position: absolute;
    font-size: 26px;
    font-weight: 400;
    color: var(--label);
  }
  .side-label--front { left: 170px; top: 100px; }
  .side-label--back { left: 916px; top: 435px; }

  .card {
    position: absolute;
    width: 540px;
    height: 360px;
    overflow: hidden;
    box-shadow: 0 4px 10px rgba(0,0,0,0.25);
  }

  /* Front */
  .card--front {
    left: 150px; top: 128px;
    background: linear-gradient(to bottom, var(--blue) 0 50%, var(--navy) 50% 100%);
  }
  .card--front .card__sheet {
    position: absolute; inset: 0;
    background: var(--white);
    border-radius: 0 190px 0 170px / 0 240px 0 130px;
  }
  .brand-lockup {
    position: absolute;
    left: 80px; top: 118px;
    display: flex; align-items: center; gap: 18px;
  }
  .brand-lockup__dot {
    width: 54px; height: 54px; border-radius: 50%;
    background: var(--brand);
  }
  .brand-lockup__name {
    font-size: 48px; font-weight: 500; color: var(--brand);
    letter-spacing: -1px;
  }
  .holder {
    position: absolute; left: 240px; top: 220px;
    line-height: 1.3;
  }
  .holder__name { font-size: 17px; font-weight: 700; color: var(--ink-name); }
  .holder__role { font-size: 17px; color: var(--ink-role); }

  /* Back */
  .card--back {
    left: 455px; top: 470px;
    background: var(--white);
  }
  .card--back .card__field {
    position: absolute; inset: 0;
    background: linear-gradient(to bottom, var(--navy) 0%, var(--navy-mid) 45%, var(--blue-light) 100%);
    border-radius: 150px 0 190px 0 / 130px 0 230px 0;
  }
  .contact {
    position: absolute; left: 132px; top: 26px;
    color: var(--white);
  }
  .social { list-style: none; margin-bottom: 22px; }
  .social__item {
    display: flex; align-items: center; gap: 8px;
    font-size: 17px; margin-bottom: 8px;
  }
  .social__icon {
    width: 32px; height: 32px; border-radius: 4px;
    background: var(--icon);
  }
  .lines { font-size: 16px; line-height: 1.3; margin-bottom: 18px; }
  .lines strong { font-weight: 700; }
  .address { font-size: 16px; line-height: 1.3; font-style: normal; }
</style>
</head>
<body>
  <span class="side-label side-label--front">Front</span>
  <span class="side-label side-label--back">Back</span>

  <section class="card card--front" aria-label="Card front">
    <div class="card__sheet"></div>
    <div class="brand-lockup">
      <span class="brand-lockup__dot"></span>
      <span class="brand-lockup__name">Pebble Reach</span>
    </div>
    <div class="holder">
      <p class="holder__name">MARK TELFORD</p>
      <p class="holder__role">CEO/Creative Director</p>
      <p class="holder__role">Pebble Reach</p>
    </div>
  </section>

  <section class="card card--back" aria-label="Card back">
    <div class="card__field"></div>
    <div class="contact">
      <ul class="social">
        <li class="social__item"><span class="social__icon"></span>social.example/pebblereach</li>
        <li class="social__item"><span class="social__icon"></span>@PebbleReach</li>
      </ul>
      <p class="lines">
        P: <strong>1 555 014 8832</strong><br>
        C: <strong>1 555 016 4907</strong><br>
        E: mark@pebblereach.example<br>
        W: www.pebblereach.example
      </p>
      <address class="address">
        318 Birchmore Avenue, Suite 207<br>
        Alderwick, LK<br>
        K7Z 4X8
      </address>
    </div>
  </section>
</body>
</html>
```